A sustainable tourism website

We are a travel/tourism company. We have developed a platform that enables organizers of sustainable theme vacations to publish and make their vacations bookable via our platform. By theme vacations, we mean vacations in categories such as Wellness, Surfing, Culinary, Martial arts, etc. We already have separate websites for each of these categories. This new website you will design is about a parent site where we provide general summary information about these individual sites and link to them. The site would be hosted on the domain velmarogo.net. Besides information about the individual sites, we also need a menu for About Us, Products and Our Climate Pledge. We also need the following at the home page:
1. A section that contain our last tweets in a twitter lightbox.
2. Summary and links to of our last few blogs.
3. A video as banner or an image. We would prefer a video though.
We already have a logo and have uploaded it. Please make sure your design conforms with our logo style and colors.
NB: We are looking for something more than the standard site you see everywhere. The winning design is a design that stands out and has a WOW effect. And when your design is selected, we intend to work with you further for the completion of the whole site.

Target Market(s)

Sustainable tourism

Number of Pages Required

1 page

Requirements
Must have
• Conform to logo design and colors.
Site must be unique, slick and stand out.
Must have a climate/sustainability blended with tourism look.
Nice to have
• Video as banner.

```html
<!DOCTYPE html>
<html lang="en">
<head>
<meta charset="utf-8">
<title>Velmaro – Sustainable Theme Vacations</title>
<link href="https://fonts.googleapis.com/css2?family=Exo+2:wght@500;600;700;800&family=Open+Sans:wght@400;600&display=swap" rel="stylesheet">
<style>
:root{
  --orange:#f07f1e;
  --orange-dark:#d96c10;
  --ink:#222222;
  --muted:#6f6f6f;
  --line:#dcdcdc;
  --paper:#ffffff;
  --mist:#f2f2f2;
  --night:#1b1b1b;
  --night-2:#2a2a2a;
  --tweet:#1d6fb8;
}
*{box-sizing:border-box;margin:0;padding:0}
html,body{width:1200px;height:4324px;overflow:hidden}
body{background:var(--paper);font-family:"Open Sans",Arial,sans-serif;color:var(--ink);position:relative}
.heading{font-family:"Exo 2",Arial,sans-serif;font-weight:700;font-size:34px;text-align:center;text-transform:uppercase;letter-spacing:.5px;color:var(--ink)}
.heading::after{content:"";display:block;width:56px;height:3px;background:var(--orange);margin:10px auto 0}

/* header */
.site-header{position:absolute;top:0;left:0;width:1200px;height:88px;display:flex;align-items:center;padding:0 140px;background:var(--paper);z-index:3}
.brand{display:flex;align-items:center;gap:10px;font-family:"Exo 2",sans-serif;font-weight:700;font-size:30px;color:var(--orange)}
.brand-dot{width:26px;height:26px;border-radius:50%;background:var(--orange)}
.main-nav{margin-left:auto;display:flex;gap:34px;font-family:"Exo 2",sans-serif;font-weight:600;font-size:15px;text-transform:uppercase}
.quote-btn{margin-left:40px;background:var(--orange);color:#fff;font-family:"Exo 2",sans-serif;font-weight:700;font-size:14px;padding:12px 26px;border-radius:24px;text-transform:uppercase}

/* hero */
.hero{position:absolute;top:88px;left:0;width:1200px;height:732px;overflow:hidden}
.hero-photo{position:absolute;inset:0;background:linear-gradient(180deg,#8fb7d6 0%,#6a9a76 35%,#3f7a52 55%,#2fa1a8 72%,#6b4a30 100%)}
.hero-content{position:absolute;top:170px;width:100%;text-align:center;color:#fff}
.hero-title{font-family:"Exo 2",sans-serif;font-weight:800;font-size:54px;letter-spacing:1px}
.hero-sub{width:520px;margin:12px auto 0;font-size:17px;line-height:26px}
.learn-btn{display:inline-block;margin-top:24px;background:var(--orange);color:#fff;font-family:"Exo 2",sans-serif;font-weight:700;font-size:15px;padding:12px 34px;border-radius:24px;text-transform:uppercase}
.hero-arrow{position:absolute;top:290px;width:36px;height:36px;border-radius:50%;background:rgba(0,0,0,.55)}
.hero-arrow.prev{left:56px}.hero-arrow.next{right:56px}
.hero-dots{position:absolute;bottom:60px;width:100%;display:flex;justify-content:center;gap:10px}
.hero-dots span{width:10px;height:10px;border-radius:50%;background:rgba(255,255,255,.6)}
.hero-dots span:first-child{background:var(--orange)}
.hero-curve{position:absolute;bottom:0;left:0}

/* categories */
.categories-title{position:absolute;top:896px;width:100%}
.category-grid{position:absolute;top:1012px;left:0;width:1200px;display:grid;grid-template-columns:592px 596px;grid-template-rows:420px 416px;gap:12px}
.category{position:relative;overflow:hidden}
.category .photo{position:absolute;inset:0}
.category .label{position:absolute;left:24px;bottom:22px;color:#fff;font-family:"Exo 2",sans-serif;font-weight:700;font-size:24px;text-transform:uppercase}
.category .go{position:absolute;right:28px;bottom:28px}
.wellness .photo{background:linear-gradient(135deg,#e9e2d8,#b99479 60%,#6b4c3b)}
.surfing .photo{background:linear-gradient(160deg,#2a6d9a,#0d4a74 55%,#072c48)}
.culinary .photo{background:linear-gradient(150deg,#4b3a2e,#8a7a62 50%,#2a2019)}
.martial .photo{background:linear-gradient(140deg,#6b4a35,#9d7a5c 50%,#3b2a20)}

/* blogs */
.blogs-title{position:absolute;top:1936px;width:100%}
.blog-list{position:absolute;top:2048px;left:144px;display:flex;gap:24px}
.blog-card{width:288px;height:432px;background:#fff;box-shadow:0 4px 18px rgba(0,0,0,.14);text-align:center;position:relative}
.blog-card .photo{height:212px}
.blog-card:nth-child(1) .photo{background:linear-gradient(160deg,#d9a56a,#8a6a4a 60%,#4d3a2c)}
.blog-card:nth-child(2) .photo{background:linear-gradient(160deg,#9bb3c7,#b84a3a 55%,#5e6a3a)}
.blog-card:nth-child(3) .photo{background:linear-gradient(180deg,#e4b372,#c9813c 45%,#3a4a32)}
.date-badge{position:absolute;top:184px;left:50%;transform:translateX(-50%);width:56px;height:56px;border-radius:50%;background:var(--orange);border:3px solid #fff;color:#fff;font-family:"Exo 2",sans-serif;font-weight:700;font-size:12px;line-height:14px;padding-top:11px}
.blog-card h3{margin:44px 22px 0;font-family:"Exo 2",sans-serif;font-weight:700;font-size:16px;line-height:21px}
.blog-card p{margin:10px 26px 0;font-size:12px;line-height:18px;color:var(--muted)}
.outline-btn{display:inline-block;margin-top:16px;border:1px solid var(--orange);color:var(--orange);font-family:"Exo 2",sans-serif;font-weight:600;font-size:12px;padding:8px 22px;text-transform:uppercase}

/* video */
.video-band{position:absolute;top:2592px;left:0;width:1200px;height:560px;background:linear-gradient(180deg,#3e4f7a 0%,#b16a7a 30%,#e3926a 45%,#4f6d8c 62%,#2b4a4a 82%,#1d2d22 100%)}
.play-btn{position:absolute;top:250px;left:570px}

/* tweets */
.tweets{position:absolute;top:3152px;left:0;width:1200px;height:616px;background:var(--mist)}
.tweets-frame{position:absolute;top:92px;left:120px;width:960px;height:440px;border:2px solid var(--line)}
.tweets-title{position:absolute;top:44px;width:100%}
.tweets-title span{background:var(--mist);padding:0 24px}
.tweet-list{position:absolute;top:200px;left:140px;display:flex;gap:20px}
.tweet-card{width:215px;height:280px;background:#fff;box-shadow:0 4px 14px rgba(0,0,0,.1);text-align:center;position:relative;padding-top:40px}
.tweet-icon{position:absolute;top:-20px;left:50%;transform:translateX(-50%);width:40px;height:40px;border-radius:50%;background:var(--tweet);border:3px solid #fff}
.tweet-card h4{font-family:"Exo 2",sans-serif;font-weight:700;font-size:14px}
.tweet-card .date{font-family:"Exo 2",sans-serif;font-weight:700;font-size:14px;margin-top:2px}
.tweet-card p{margin:12px 18px 0;font-size:12px;line-height:18px;color:var(--muted)}
.tweet-actions{position:absolute;bottom:18px;width:100%;display:flex;justify-content:center;gap:20px}
.tweet-actions span{width:10px;height:8px;background:#b8b8b8;border-radius:2px}
.tweet-dots{position:absolute;top:538px;width:100%;display:flex;justify-content:center;gap:10px}
.tweet-dots span{width:10px;height:10px;border-radius:50%;background:#c9c9c9}
.tweet-dots span:first-child{background:var(--orange)}

/* footer */
.site-footer{position:absolute;top:3768px;left:0;width:1200px;height:556px;background:var(--night);color:#e6e6e6}
.footer-col{position:absolute;top:62px}
.footer-col h5{font-family:"Exo 2",sans-serif;font-weight:700;font-size:16px;text-transform:uppercase;color:#fff;margin-bottom:26px}
.contact{left:140px}
.contact li{list-style:none;display:flex;gap:16px;font-size:13px;line-height:19px;margin-bottom:18px}
.quick{left:520px}
.quick li{list-style:none;font-size:13px;line-height:24px}
.newsletter{left:780px;width:300px}
.field{height:40px;border:1px solid #555;margin-bottom:16px;padding:10px 12px;font-size:13px;color:#aaa}
.subscribe{display:inline-block;background:var(--orange);color:#fff;font-family:"Exo 2",sans-serif;font-weight:700;font-size:13px;padding:10px 26px;text-transform:uppercase}
.footer-bottom{position:absolute;top:400px;left:0;width:100%;border-top:1px solid var(--night-2);text-align:center;padding-top:36px}
.social{display:flex;justify-content:center;gap:12px}
.social span{width:30px;height:30px;border-radius:50%;border:2px solid var(--orange)}
.copyright{margin-top:22px;font-size:12px;color:#bdbdbd}
</style>
</head>
<body>

<header class="site-header">
  <div class="brand"><span class="brand-dot"></span>velmaro</div>
  <nav class="main-nav"><span>Home</span><span>Products</span><span>About Us</span><span>Our Climate Pledge</span></nav>
  <span class="quote-btn">Request a Quote</span>
</header>

<section class="hero">
  <div class="hero-photo" role="img" aria-label="Traveller sitting on a longtail boat between green limestone cliffs and turquoise water"></div>
  <div class="hero-content">
    <h1 class="hero-title">VELMARO</h1>
    <p class="hero-sub">Slow journeys to wild places, planned with care for people, nature and the climate we all share.</p>
    <span class="learn-btn">Learn More</span>
  </div>
  <svg class="hero-arrow prev" viewBox="0 0 36 36"><path d="M20 12l-6 6 6 6" stroke="#fff" stroke-width="2.5" fill="none"/></svg>
  <svg class="hero-arrow next" viewBox="0 0 36 36"><path d="M16 12l6 6-6 6" stroke="#fff" stroke-width="2.5" fill="none"/></svg>
  <div class="hero-dots"><span></span><span></span><span></span></div>
  <svg class="hero-curve" width="1200" height="120" viewBox="0 0 1200 120">
    <path d="M0 40 Q600 150 1200 40 L1200 120 L0 120Z" fill="#fff"/>
    <path d="M0 40 Q600 150 1200 40" stroke="var(--orange)" stroke-width="6" fill="none"/>
  </svg>
</section>

<h2 class="heading categories-title">Our Vacation Categories</h2>
<section class="category-grid">
  <a class="category wellness"><div class="photo" role="img" aria-label="Two friends relaxing in robes at a spa"></div><span class="label">Wellness</span>
    <svg class="go" width="22" height="12" viewBox="0 0 22 12"><path d="M0 6h20M15 1l5 5-5 5" stroke="#fff" stroke-width="2" fill="none"/></svg></a>
  <a class="category surfing"><div class="photo" role="img" aria-label="Surfer riding inside a breaking ocean wave"></div><span class="label">Surfing</span>
    <svg class="go" width="22" height="12" viewBox="0 0 22 12"><path d="M0 6h20M15 1l5 5-5 5" stroke="#fff" stroke-width="2" fill="none"/></svg></a>
  <a class="category culinary"><div class="photo" role="img" aria-label="Chef pouring olive oil over a plated dish"></div><span class="label">Culinary</span>
    <svg class="go" width="22" height="12" viewBox="0 0 22 12"><path d="M0 6h20M15 1l5 5-5 5" stroke="#fff" stroke-width="2" fill="none"/></svg></a>
  <a class="category martial"><div class="photo" role="img" aria-label="Two martial artists in white uniforms sparring in a dojo"></div><span class="label">Martial Arts</span>
    <svg class="go" width="22" height="12" viewBox="0 0 22 12"><path d="M0 6h20M15 1l5 5-5 5" stroke="#fff" stroke-width="2" fill="none"/></svg></a>
</section>

<h2 class="heading blogs-title">Our Last Blogs</h2>
<section class="blog-list">
  <article class="blog-card"><div class="photo" role="img" aria-label="Hikers on a forest trail in warm light"></div><div class="date-badge">22<br>SEP</div>
    <h3>Walking the quiet rice terraces of northern hills</h3>
    <p>Small guesthouses, local guides and meals grown a few steps from the table.</p><span class="outline-btn">Read More</span></article>
  <article class="blog-card"><div class="photo" role="img" aria-label="Red train crossing a mountain valley"></div><div class="date-badge">22<br>SEP</div>
    <h3>Crossing the mountains by rail instead of plane</h3>
    <p>Small guesthouses, local guides and meals grown a few steps from the table.</p><span class="outline-btn">Read More</span></article>
  <article class="blog-card"><div class="photo" role="img" aria-label="Palm trees on a beach at sunset"></div><div class="date-badge">22<br>SEP</div>
    <h3>A week of reef care on a small island coast</h3>
    <p>Small guesthouses, local guides and meals grown a few steps from the table.</p><span class="outline-btn">Read More</span></article>
</section>

<section class="video-band" role="img" aria-label="Video banner: misty mountain ranges at dusk above a hillside town">
  <svg class="play-btn" width="60" height="60" viewBox="0 0 60 60"><circle cx="30" cy="30" r="30" fill="#fff"/><path d="M24 18l18 12-18 12z" fill="#1b2a44"/></svg>
</section>

<section class="tweets">
  <div class="tweets-frame"></div>
  <h2 class="heading tweets-title"><span>Our Last Tweets</span></h2>
  <div class="tweet-list">
    <div class="tweet-card"><span class="tweet-icon"></span><h4>Pledge update shared</h4><div class="date">22 Sep 2020</div>
      <p>This season every booking plants native trees with our partners, and new surf trips now travel by train.</p>
      <div class="tweet-actions"><span></span><span></span><span></span></div></div>
    <div class="tweet-card"><span class="tweet-icon"></span><h4>New wellness retreats</h4><div class="date">22 Sep 2020</div>
      <p>This season every booking plants native trees with our partners, and new surf trips now travel by train.</p>
      <div class="tweet-actions"><span></span><span></span><span></span></div></div>
    <div class="tweet-card"><span class="tweet-icon"></span><h4>Cooking with locals</h4><div class="date">22 Sep 2020</div>
      <p>This season every booking plants native trees with our partners, and new surf trips now travel by train.</p>
      <div class="tweet-actions"><span></span><span></span><span></span></div></div>
    <div class="tweet-card"><span class="tweet-icon"></span><h4>Dojo stays open</h4><div class="date">22 Sep 2020</div>
      <p>This season every booking plants native trees with our partners, and new surf trips now travel by train.</p>
      <div class="tweet-actions"><span></span><span></span><span></span></div></div>
  </div>
  <div class="tweet-dots"><span></span><span></span></div>
</section>

<footer class="site-footer">
  <div class="footer-col contact">
    <h5>Contact Us</h5>
    <ul>
      <li><svg width="14" height="18" viewBox="0 0 14 18"><path d="M7 0a7 7 0 0 0-7 7c0 5 7 11 7 11s7-6 7-11a7 7 0 0 0-7-7z" fill="#fff"/><circle cx="7" cy="7" r="2.5" fill="#1b1b1b"/></svg><span>Velmaro<br>220 Harbour Lane<br>Westfield 4021</span></li>
      <li><svg width="14" height="16" viewBox="0 0 14 16"><path d="M3 0l3 4-2 2c1 2 3 4 5 5l2-2 3 3-2 3C6 15-1 8 0 2z" fill="#fff"/></svg><span>Phone:<br>555-0142-8890</span></li>
      <li><svg width="16" height="12" viewBox="0 0 16 12"><rect width="16" height="12" fill="#fff"/><path d="M0 0l8 6 8-6" stroke="#1b1b1b" fill="none"/></svg><span>Email:<br>info@velmarogo.net</span></li>
    </ul>
  </div>
  <div class="footer-col quick">
    <h5>Quick Links</h5>
    <ul><li>Home</li><li>About Us</li><li>Our Products</li><li>Our Climate Pledge</li><li>Contact</li></ul>
  </div>
  <div class="footer-col newsletter">
    <h5>Sign Up For Newsletter</h5>
    <div class="field">Name</div>
    <div class="field">Email</div>
    <span class="subscribe">Subscribe</span>
  </div>
  <div class="footer-bottom">
    <div class="social"><span></span><span></span><span></span><span></span></div>
    <p class="copyright">Velmaro © 2020 All Rights Reserved | Privacy Policy</p>
  </div>
</footer>

</body>
</html>
```